Business Card Design Project

I am a psychotherapist, counselor and expressive arts therapist (means I use every art form imaginable in the service of healing). I'm just starting out in private practice in San Francisco, CA. I work with individual adults, children and families. I'd like the card to mirror the simplicity and color palate of my website. I also would love if there is a symbol, image of fire, flame or spark (that is warming, not frightening).

Check out my website: www.lorabeckettmft.com

I want the cards to be printed in letter press so please keep that in mind!

Target Market(s)

Upper Middle Class Adults who are progressively minded, artistic or artists, open to psychotherapy, interested in health & healing.

Industry/Entity Type

Business

Requirements
Must have
• Text to be included:

Lora Beckett
Counseling, Psychotherapy & Expressive Arts

2814 Wexford Avenue, Suite F
San Francisco, CA 94127
p. 415.862.3097
lorajanebeckett@mailvane.net

www.lorabeckettmft.com

MFT License Number 68947

It's OK to abbreviate Number to # or Street to St., etc.

Must be compatible with letter press printing.
Nice to have
• I don't have a logo. I don't expect designers to necessarily create one for me, but if someone comes up with a simple image (see above about flame), that would be great. I don't have much of a budget now, but expect that to change in the next year or so and then could buy a logo for my website, future letterhead, etc.

```html
<!DOCTYPE html>
<html lang="en">
<head>
<meta charset="utf-8">
<title>Lora Beckett — Business Card</title>
<link rel="stylesheet" href="https://fonts.googleapis.com/css2?family=Josefin+Slab:wght@400;600&display=swap">
<style>
  :root {
    --backdrop: #e9e9e8;
    --card: #f4f4f2;
    --crimson: #b3333f;
    --ember: #b8432c;
    --card-shadow: rgba(0, 0, 0, 0.12);
  }
  html, body {
    margin: 0;
    padding: 0;
    width: 1200px;
    height: 799px;
    overflow: hidden;
    background: var(--backdrop);
  }
  .stage {
    width: 1200px;
    height: 799px;
    display: flex;
    align-items: center;
    justify-content: center;
  }
  .business-card {
    width: 840px;
    height: 480px;
    background: var(--card);
    box-shadow: 0 10px 30px var(--card-shadow);
    box-sizing: border-box;
    padding: 48px 70px 40px;
    display: flex;
    flex-direction: column;
    align-items: center;
    font-family: "Josefin Slab", Georgia, serif;
    color: var(--crimson);
    text-align: center;
  }
  .brand-mark {
    display: flex;
    align-items: center;
    gap: 10px;
    font-size: 18px;
    font-weight: 600;
    letter-spacing: 0.18em;
    color: var(--ember);
    margin-bottom: 18px;
  }
  .brand-dot {
    width: 14px;
    height: 14px;
    border-radius: 50%;
    background: var(--ember);
  }
  .practice-name {
    margin: 0;
    font-size: 60px;
    font-weight: 400;
    letter-spacing: 0.06em;
    line-height: 1;
  }
  .name-rule {
    width: 620px;
    height: 3px;
    background: var(--ember);
    margin: 8px 0 10px;
  }
  .practice-tagline {
    margin: 0 0 30px;
    font-size: 24px;
  }
  .contact-details {
    font-style: normal;
    font-size: 25px;
    line-height: 1.28;
  }
  .contact-details p {
    margin: 0;
  }
</style>
</head>
<body>
  <main class="stage">
    <section class="business-card">
      <div class="brand-mark">
        <span class="brand-dot"></span>
        <span>LORA BECKETT</span>
      </div>
      <h1 class="practice-name">LORABECKETT</h1>
      <div class="name-rule"></div>
      <p class="practice-tagline">Counseling, Psychotherapy &amp; Expressive Arts</p>
      <address class="contact-details">
        <p>2814 Wexford Ave, Suite F San Francisco, CA 94127</p>
        <p>P.415.862.3097</p>
        <p>lorajanebeckett@mailvane.net</p>
        <p>www.lorabeckettmft.com</p>
        <p>MFT License #68947</p>
      </address>
    </section>
  </main>
</body>
</html>
```